Veltorquin.io - Please redesign to make it look better from current design

We already have the current website, that you can access but we think it can improve from current version.
Veltorquin is a cryptocurrency hedge fund that allow you to participate in the hedge fund with cryptocurrency such as eth.
At current phase, we are doing an ICO, then we want to make sure that the website it looks professional, beautiful and trustable enough for investors after looking at our website.
Target Market(s)
Investors
Industry/Entity Type
Investment
Coding
Coded - Design and coding required
Number of Pages Required
1 page
Look and feel

```html
<!DOCTYPE html>
<html lang="en">
<head>
<meta charset="utf-8">
<title>Veltorquin – Digital Asset Management</title>
<link rel="stylesheet" href="https://fonts.googleapis.com/css2?family=Open+Sans:wght@400;600&display=swap">
<style>
  :root {
    --hero-from: #3446a8;
    --hero-to: #5d6fd0;
    --white: #ffffff;
    --ink: #1c1c1c;
    --body-text: #555a60;
    --navy: #1d2f6e;
    --team-bg: #d5e8f3;
    --pill: #bfe6fb;
    --cta: #0a8fcf;
    --footer: #191919;
    --footer-line: #8a8a8a;
    --accent-blue: #2d5be3;
  }
  * { box-sizing: border-box; margin: 0; padding: 0; }
  html, body { width: 1200px; height: 2276px; overflow: hidden; }
  body { font-family: "Open Sans", Arial, sans-serif; color: var(--ink); background: var(--white); position: relative; }
  h1, h2 { font-weight: 400; }

  /* Hero */
  .hero { position: absolute; left: 0; top: 0; width: 1200px; height: 583px;
    background: linear-gradient(120deg, var(--hero-from) 0%, var(--hero-to) 100%); color: var(--white); }
  .brand { position: absolute; left: 88px; top: 56px; display: flex; align-items: center; gap: 10px;
    font-size: 26px; font-weight: 600; color: var(--white); }
  .brand-dot { width: 30px; height: 30px; border-radius: 50%; background: var(--white); }
  .nav { position: absolute; top: 55px; left: 0; width: 1200px; height: 27px; }
  .nav a { position: absolute; top: 0; height: 27px; line-height: 27px; font-size: 16px; color: var(--white); text-decoration: none; }
  .nav a.active { background: var(--pill); color: var(--navy); border-radius: 14px; width: 82px; text-align: center; }
  .hero-title { position: absolute; left: 88px; top: 252px; font-size: 56px; font-weight: 600; line-height: 1; letter-spacing: 1px; }
  .hero-sub { position: absolute; left: 88px; top: 314px; font-size: 29px; font-weight: 400; }
  .hero-visual { position: absolute; left: 655px; top: 162px; width: 398px; height: 336px; border-radius: 8px;
    background: linear-gradient(180deg, #0f2260 0%, #0f2260 72%, #e6e6e8 72%, #cfcfd3 100%); }
  .pager { position: absolute; left: 1150px; top: 254px; display: flex; flex-direction: column; gap: 11px; }
  .pager span { width: 6px; height: 6px; border-radius: 50%; background: var(--white); }

  /* Definition */
  .definition-icon { position: absolute; left: 546px; top: 652px; width: 103px; height: 99px; border-radius: 10px;
    background: linear-gradient(135deg, #dfeaf3, #9ccbea); }
  .section-title { position: absolute; left: 0; width: 1200px; text-align: center; font-size: 31px; font-weight: 400; color: var(--ink); letter-spacing: 0.5px; }
  .definition-text { position: absolute; left: 160px; top: 834px; width: 880px; text-align: center;
    font-size: 13.6px; line-height: 21.5px; color: var(--body-text); letter-spacing: -0.1px; }

  /* Team */
  .team { position: absolute; left: 0; top: 1004px; width: 1200px; height: 562px; background: var(--team-bg); }
  .member { position: absolute; top: 146px; width: 260px; text-align: center; }
  .member-photo { width: 180px; height: 180px; margin: 0 auto; border-radius: 50%; border: 3px solid var(--white);
    background: linear-gradient(160deg, #6b5548, #2e2a2c); }
  .member-name { margin-top: 38px; font-size: 17px; color: var(--navy); letter-spacing: 0.3px; white-space: nowrap; }
  .member-role { margin-top: 2px; font-size: 16px; color: var(--navy); }
  .member-bio { margin: 8px auto 0; width: 256px; font-size: 12.5px; line-height: 20px; color: var(--ink); }

  /* Process */
  .process-art { position: absolute; left: 88px; top: 1661px; width: 334px; height: 243px;
    background: linear-gradient(180deg, #ffffff 0%, #e1f1fb 55%, #cfe6f8 100%); border-bottom: 3px solid var(--accent-blue); }
  .process-kicker { position: absolute; left: 490px; top: 1670px; font-size: 21px; color: var(--navy); }
  .process-title { position: absolute; left: 490px; top: 1698px; font-size: 28px; font-weight: 400; color: var(--ink); letter-spacing: 0.5px; }
  .process-text { position: absolute; left: 490px; top: 1743px; width: 604px; font-size: 14px; line-height: 24px; color: var(--body-text); }
  .btn-outline { position: absolute; left: 491px; top: 1866px; width: 101px; height: 35px; border: 1.5px solid var(--navy);
    border-radius: 18px; font-size: 11px; line-height: 32px; text-align: center; color: var(--navy); }

  /* CTA */
  .cta { position: absolute; left: 0; top: 1990px; width: 1200px; height: 115px; background: var(--cta); }
  .cta-label { position: absolute; left: 296px; top: 37px; font-size: 23px; color: var(--white); letter-spacing: 0.5px; }
  .cta-button { position: absolute; left: 640px; top: 34px; width: 261px; height: 50px; border-radius: 25px; background: var(--white);
    font-size: 18px; line-height: 50px; text-align: center; color: #333; }

  /* Footer */
  .footer { position: absolute; left: 0; top: 2105px; width: 1200px; height: 171px; background: var(--footer); color: var(--white); }
  .footer-links { position: absolute; top: 44px; left: 0; width: 1200px; text-align: center; font-size: 12px; word-spacing: 4px; }
  .social { position: absolute; top: 76px; left: 500px; width: 200px; display: flex; gap: 8px; justify-content: center; }
  .social span { width: 27px; height: 27px; border-radius: 50%; border: 1.5px solid var(--footer-line); display: flex; align-items: center; justify-content: center; }
  .copyright { position: absolute; top: 118px; left: 0; width: 1200px; text-align: center; font-size: 12px; }
</style>
</head>
<body>

<header class="hero">
  <div class="brand"><span class="brand-dot"></span>Veltorquin</div>
  <nav class="nav">
    <a class="active" style="left:449px">HOME</a>
    <a style="left:564px">ABOUT US</a>
    <a style="left:698px">SERVICES</a>
    <a style="left:819px">PROJECTS</a>
    <a style="left:945px">BLOG</a>
    <a style="left:1036px">CONTACT</a>
  </nav>
  <h1 class="hero-title">VELTORQUIN</h1>
  <p class="hero-sub">Digital Asset Management</p>
  <div class="hero-visual" role="img" aria-label="Illustration of a desktop monitor displaying the Veltorquin name"></div>
  <div class="pager"><span></span><span></span><span></span><span></span><span></span></div>
</header>

<section>
  <div class="definition-icon" role="img" aria-label="Wallet icon with a coin"></div>
  <h2 class="section-title" style="top:786px">DEFINITION</h2>
  <p class="definition-text">Veltorquin process and manages on hedge fund strategy models which invests in a diversified portfolio of blockchain tokens. Block-chain tokens are emerging which add a monetary incentive layer to p2p protocols and facilitate equity crowdfunding that anyone in the world can participate in. This means open source software developers can monetize their networks at the protocol level and users of the network are the equity owners of the network. For this conditions, returns will go to holders of the tokens.</p>
</section>

<section class="team">
  <h2 class="section-title" style="top:66px">EXECUTIVE TEAM</h2>
  <div class="member" style="left:128px">
    <div class="member-photo" role="img" aria-label="Portrait photo of the director"></div>
    <div class="member-name">KASEMRAT RAVENDEL</div>
    <div class="member-role">Director</div>
    <p class="member-bio">As a hedge fund manager. Ravendel is the Chief Executive Officer of Northbay Capital LLC, an investment manager</p>
  </div>
  <div class="member" style="left:474px">
    <div class="member-photo" role="img" aria-label="Portrait photo of the technical advisor" style="background:linear-gradient(160deg,#b9c2a4,#6f7762)"></div>
    <div class="member-name">TANAWUT LORSIRI</div>
    <div class="member-role">Technical advisor</div>
    <p class="member-bio">Lorsiri has various experienced on crypto-currency and blockchain technology. He created what was the world's 4th</p>
  </div>
  <div class="member" style="left:815px">
    <div class="member-photo" role="img" aria-label="Portrait photo of the marketing consultant" style="background:linear-gradient(160deg,#7a3a26,#3a1c14)"></div>
    <div class="member-name">PHAKORN WIRATSOMBAT</div>
    <div class="member-role">Marketing Consultant</div>
    <p class="member-bio">Wiratsombat embeds a decade of expe-rience in brand building, strategic planning, and marketing communication across</p>
  </div>
</section>

<section>
  <div class="process-art" role="img" aria-label="Line illustration of a rocket launching from a computer screen beside a cactus and a coffee cup"></div>
  <div class="process-kicker">PROCESS</div>
  <h2 class="process-title">HEDGE FUND MODEL</h2>
  <p class="process-text">Veltorquin run on closed-end fund （CEF）model which offers its shares to investors and utilize the fund to speculate and invest in the innovative blockchain tokens. Veltorquin will charge an upfront annual operation fee 4% of the money raised during the ICO. After that, the fund will charge a quarterly performance of 50% on the net profit made.</p>
  <div class="btn-outline">READ MORE »</div>
</section>

<section class="cta">
  <div class="cta-label">FOR MORE INFORMATION</div>
  <div class="cta-button">DOWNLOAD WHITEPAPER</div>
</section>

<footer class="footer">
  <div class="footer-links">ABOUT &nbsp;| &nbsp;PRIVACY &nbsp;| &nbsp;TERMS &nbsp;| &nbsp;LEGAL &nbsp;| &nbsp;CONTACT</div>
  <div class="social">
    <span></span><span></span><span></span><span></span><span></span>
    <span><svg width="13" height="10" viewBox="0 0 13 10"><rect x="0.75" y="0.75" width="11.5" height="8.5" rx="1" fill="none" stroke="#8a8a8a" stroke-width="1.2"/><path d="M1 1.2 6.5 5.5 12 1.2" fill="none" stroke="#8a8a8a" stroke-width="1.2"/></svg></span>
  </div>
  <div class="copyright">Copyright © 2017 &nbsp;All Rights Reserved</div>
</footer>

</body>
</html>
```